QXT website video quote promotion tiles

We are promoting vehicle leasing by video, which contains several quotation examples imported from the video. We must re-vamp the quotation tiles, contact boxes, and contact form. The first tile is generated from the video, so this must be a separate project. We are looking for a welcoming, professional flow and leave color choices to design with an emphasis on communication prompts, and additional prompts in the design would be welcome.

Target Market(s)

Any Customer interaction from the tile quotes, contact, call, message,

Industry/Entity Type

vehicle leasing

Coding

Coded - Design and coding required

Number of Pages Required

1 page

Colors

Designer to choose colors to be used in the design.

Requirements
Must have
• emphasis on point of contact and visual impact on quote tile excluding main one
Should not have
• changes to the quote structure as these imported from video pricing no changes to main image as this template which can addressed as separate project

```html
<!DOCTYPE html>
<html lang="en">
<head>
<meta charset="UTF-8">
<title>QXT Quote Tiles and Contact Form</title>
<link href="https://fonts.googleapis.com/css2?family=Montserrat:wght@500;700;800&family=Mulish:wght@400;700;800&display=swap" rel="stylesheet">
<style>
  :root {
    --page-bg: #58595b;
    --panel-bg: #414141;
    --card-bg: #f5f3f3;
    --orange: #e6894c;
    --yellow: #ebbe42;
    --green: #2aa81c;
    --peach: #f2c8b0;
    --ink: #232323;
    --white: #ffffff;
  }
  * { box-sizing: border-box; margin: 0; padding: 0; }
  html, body { width: 1200px; height: 1141px; overflow: hidden; }
  body { background: var(--page-bg); font-family: "Mulish", sans-serif; position: relative; }

  .quote-tile { position: absolute; top: 47px; width: 547px; height: 392px; background: var(--card-bg); }
  .quote-tile--classic { left: 47px; }
  .quote-tile--featured { left: 612px; }

  .tile-title { font-family: "Montserrat", sans-serif; font-weight: 800; font-size: 33px; text-align: center; letter-spacing: 0.3px; }
  .tile-price { font-family: "Montserrat", sans-serif; font-weight: 800; font-size: 45px; letter-spacing: -1px; }
  .vat-tag { display: inline-block; background: var(--white); font-family: "Montserrat", sans-serif; font-weight: 800; font-size: 20px; line-height: 33px; padding: 0 9px; }
  .tile-terms { font-family: "Mulish", sans-serif; font-weight: 800; font-size: 28px; text-align: center; }
  .maintenance-pill { position: absolute; left: 50%; transform: translateX(-50%); font-family: "Mulish", sans-serif; color: var(--ink); white-space: nowrap; }

  /* classic tile */
  .classic-header { height: 173px; background: var(--orange); color: var(--white); padding-top: 33px; }
  .classic-header .price-row { display: flex; justify-content: center; align-items: center; gap: 18px; margin-top: 20px; }
  .classic-header .vat-tag { color: var(--orange); }
  .quote-tile--classic .tile-terms { color: var(--orange); margin-top: 20px; }
  .quote-tile--classic .maintenance-pill { top: 248px; width: 192px; height: 43px; line-height: 43px; text-align: center; background: var(--white); border-radius: 22px; font-size: 22px; }

  /* featured tile */
  .quote-tile--featured .tile-title { color: var(--ink); padding-top: 33px; }
  .price-banner { position: absolute; left: 108px; top: 93px; width: 332px; height: 58px; display: flex; align-items: center; justify-content: center; gap: 12px; color: var(--white); }
  .price-banner svg { position: absolute; inset: 0; z-index: 0; }
  .price-banner > span { position: relative; z-index: 1; }
  .price-banner .tile-price { font-size: 42px; }
  .price-banner .vat-tag { color: var(--yellow); font-size: 19px; line-height: 29px; }
  .featured-band { position: absolute; top: 178px; left: 0; width: 100%; height: 97px; background: var(--orange); color: var(--white); padding-top: 21px; }
  .quote-tile--featured .maintenance-pill { top: 251px; width: 164px; height: 38px; line-height: 38px; text-align: center; background: var(--peach); border-radius: 19px; font-size: 18px; }

  .tile-actions { position: absolute; left: 23px; right: 23px; top: 318px; height: 54px; display: flex; gap: 13px; }
  .action-btn { flex: 1; display: flex; align-items: center; justify-content: center; gap: 14px; color: var(--white); font-family: "Montserrat", sans-serif; font-weight: 800; font-size: 19px; text-decoration: none; }
  .action-btn--contact { background: var(--yellow); }
  .action-btn--chat { background: var(--green); }
  .quote-tile--featured .action-btn { border-radius: 27px; }
  .chat-dot { width: 28px; height: 28px; border-radius: 50%; background: var(--white); }

  /* contact form */
  .contact-panel { position: absolute; left: 46px; top: 483px; width: 1107px; height: 603px; background: var(--panel-bg); }
  .contact-heading { position: absolute; top: 52px; width: 100%; text-align: center; color: var(--white); font-family: "Montserrat", sans-serif; font-weight: 800; font-size: 28px; letter-spacing: 0.2px; }
  .heading-rule { position: absolute; top: 116px; left: 500px; width: 94px; height: 2px; background: var(--white); }
  .field { position: absolute; background: var(--card-bg); border-radius: 8px; font-family: "Mulish", sans-serif; font-size: 15px; color: var(--ink); padding: 18px 19px; }
  .field--name { left: 80px; top: 171px; width: 462px; height: 52px; }
  .field--email { left: 561px; top: 171px; width: 463px; height: 52px; }
  .field--phone { left: 80px; top: 242px; width: 462px; height: 52px; }
  .field--subject { left: 561px; top: 242px; width: 463px; height: 52px; }
  .field--message { left: 80px; top: 313px; width: 944px; height: 156px; }
  .submit-btn { position: absolute; left: 466px; top: 505px; width: 177px; height: 55px; background: var(--orange); border-radius: 6px; color: var(--white); font-family: "Montserrat", sans-serif; font-weight: 800; font-size: 24px; display: flex; align-items: center; justify-content: center; }
</style>
</head>
<body>

<section class="quote-tile quote-tile--classic">
  <div class="classic-header">
    <h2 class="tile-title">CONTRACT HIRE</h2>
    <div class="price-row">
      <span class="tile-price">£247.33</span>
      <span class="vat-tag">PLUS VAT</span>
    </div>
  </div>
  <p class="tile-terms">3 years, 9+35, 10K miles annually</p>
  <span class="maintenance-pill">Not Maintained</span>
  <div class="tile-actions">
    <a class="action-btn action-btn--contact">
      <svg width="24" height="17" viewBox="0 0 24 17"><rect x="1" y="1" width="22" height="15" fill="none" stroke="#fff" stroke-width="2"/><path d="M1 1 L12 10 L23 1 M1 16 L9 8 M23 16 L15 8" fill="none" stroke="#fff" stroke-width="2"/></svg>
      <span>CONTACT US</span>
    </a>
    <a class="action-btn action-btn--chat"><span class="chat-dot"></span><span>CHATLINE</span></a>
  </div>
</section>

<section class="quote-tile quote-tile--featured">
  <h2 class="tile-title">CONTRACT HIRE</h2>
  <div class="price-banner">
    <svg width="332" height="58" viewBox="0 0 332 58"><polygon points="10,0 322,0 332,58 0,58" fill="#ebbe42"/></svg>
    <span class="tile-price">£247.33</span>
    <span class="vat-tag">PLUS VAT</span>
  </div>
  <div class="featured-band">
    <p class="tile-terms">3 years, 9+35, 10K miles annually</p>
  </div>
  <span class="maintenance-pill">Not Maintained</span>
  <div class="tile-actions">
    <a class="action-btn action-btn--contact">
      <svg width="24" height="17" viewBox="0 0 24 17"><rect x="1" y="1" width="22" height="15" fill="none" stroke="#fff" stroke-width="2"/><path d="M1 1 L12 10 L23 1 M1 16 L9 8 M23 16 L15 8" fill="none" stroke="#fff" stroke-width="2"/></svg>
      <span>CONTACT US</span>
    </a>
    <a class="action-btn action-btn--chat"><span class="chat-dot"></span><span>CHATLINE</span></a>
  </div>
</section>

<section class="contact-panel">
  <h2 class="contact-heading">PLEASE SUBMIT YOUR CONTACT DETAILS</h2>
  <div class="heading-rule"></div>
  <div class="field field--name">Your Name</div>
  <div class="field field--email">Your Email</div>
  <div class="field field--phone">Contact Number</div>
  <div class="field field--subject">Subject</div>
  <div class="field field--message">Message</div>
  <div class="submit-btn">SUBMIT</div>
</section>

</body>
</html>
```